Web design for community centre - bright colours (provided) and matching existing logo

Website based on a provided logo and existing website template skeleton (it is a Wordpress theme we must use that is already installed)

Basically, see if you can improve the existing theme skeleton at https://tarvolnh.org.au/redesign/. Mostly we are looking for a much nicer menu that works with the logo, and a nice font/design for text content.

We have a developer who will work your design into the Wordpress theme – so you can get creative in a graphic software app and our developer can most likely implement your ideas.

The website ideally will include design ideas from the logo (e.g. the idea of people with their arms around each other, colours).

Improvement to the text displayed on the photo slider (e.g. a colour border or other decoration) is also needed.

It needs a 'community' feel.

Target Market(s)

Parents (provides childcare), older people, people with disabilities, recent migrants

Industry/Entity Type

Community Center

Number of Pages Required

1 page

Font styles to use
Sans Serif

Colors

Designer to choose colors to be used in the design.

Requirements
Must have
• A very aesthetic top menu. Nice use of spacing, negative space etc.
• Fonts need to be legally available without a pageview fee (one off purchase OK). You need to provide proof we can use the font legally.
• See https://www.pelmoray.org.au/ for an example of a menu we like.
• Must use the existing logo, provided in this brief.
• Needs to use colours from the logo but do not need to use all of them!
• Must be workable into the theme already installed at https://tarvolnh.org.au/redesign
Nice to have
• Maybe some kind of shapes attached to each menu link (top menu0
• A use of all 5 colours on the top menu, when you hover on it
Should not have
• Serif fonts

```html
<!DOCTYPE html>
<html lang="en">
<head>
<meta charset="utf-8">
<title>Tarvol Neighbourhood Learning Centre</title>
<link rel="stylesheet" href="https://fonts.googleapis.com/css2?family=Jost:wght@400;500;600&display=swap">
<style>
:root{
  --ink:#1f1f1f;
  --grey:#555;
  --orange:#f7931e;
  --lime:#b5e26c;
  --pink:#ec1e79;
  --blue:#00aeef;
  --white:#fff;
  --line:#d0d0d0;
}
*{box-sizing:border-box;margin:0;padding:0}
html,body{width:1200px;height:2993px;overflow:hidden;background:var(--white)}
body{position:relative;font-family:'Jost',sans-serif;color:var(--ink)}
.abs{position:absolute}
a{color:inherit;text-decoration:none}
.arrow{display:inline-block;vertical-align:middle;margin-left:10px}

/* header */
.contact{left:107px;top:36px;font-size:14px;line-height:23px}
.contact b{font-weight:500}
.brand{left:472px;top:24px;display:flex;align-items:center;gap:12px}
.brand-dot{width:72px;height:72px;border-radius:50%;border:8px solid var(--orange)}
.brand-name{font-size:22px;font-weight:500;line-height:24px;width:180px}
.search{left:839px;top:46px;width:253px;border-bottom:1px solid #999;font-size:14px;padding:0 4px 6px;display:flex;justify-content:space-between}
.nav{left:163px;top:120px;display:flex;align-items:center;font-size:17px;color:#444}
.nav a{padding:9px 14px;border-radius:22px;margin-right:3px}
.nav a.active{background:var(--orange);color:var(--white);padding:9px 23px}

/* hero */
.donate{left:0;top:185px;width:397px;height:550px;background:var(--lime)}
.donate h2{position:absolute;left:107px;top:155px;font-weight:400;font-size:34px;line-height:38px;color:#333}
.donate p{position:absolute;left:103px;top:260px;width:240px;font-size:16px;line-height:21px;color:#333}
.donate .link{position:absolute;left:107px;top:364px;font-size:18px;border-bottom:2px solid #333;padding:0 2px 4px 2px;color:#333}
.hero-photo{left:397px;top:185px;width:803px;height:550px;background:linear-gradient(120deg,#8fb7d6 0%,#e7c7a8 45%,#d69a6e 70%,#7ea5cc 100%)}
.hero-nav{left:1088px;top:418px}
.hero-card{left:809px;top:497px;width:364px;height:238px;background:var(--white)}
.hero-card h3{position:absolute;left:31px;top:28px;font-weight:400;font-size:30px;line-height:31px}
.hero-card p{position:absolute;left:31px;top:102px;width:310px;font-size:14px;line-height:21px;color:var(--grey)}
.btn-pink{position:absolute;left:27px;top:183px;width:202px;height:41px;background:var(--pink);color:var(--white);border-radius:21px;font-size:14px;font-weight:500;display:flex;align-items:center;padding-left:21px;gap:9px}

/* courses */
.section-title{left:107px;top:860px;font-size:25px;font-weight:400}
.btn-outline{left:319px;top:860px;width:155px;height:36px;border:2px solid var(--pink);border-radius:18px;color:var(--pink);font-size:15px;font-weight:500;display:flex;align-items:center;justify-content:center}
.pager{top:869px;width:39px;height:31px;border:2px solid var(--ink);display:flex;align-items:center;justify-content:center}
.course{top:921px;height:252px;border:1px solid var(--line)}
.course .thumb{height:188px}
.course span{position:absolute;left:0;right:0;top:208px;text-align:center;font-size:18px}

/* video */
.video{left:0;width:1200px;top:1287px;text-align:center;font-size:24px;line-height:31px;color:#333}
.video-link{left:526px;top:1374px;font-size:18px;border-bottom:2px solid var(--ink);padding:0 5px 2px}

/* grid */
.tile-blue{left:79px;top:1487px;width:279px;height:287px;background:var(--blue);color:var(--white)}
.tile-blue h4{position:absolute;left:51px;top:117px;font-weight:400;font-size:21px;line-height:24px}
.tile-blue a{position:absolute;left:52px;top:186px;font-size:13px;font-weight:600;border-bottom:2px solid var(--white);padding-bottom:3px;letter-spacing:.5px}
.photo-hands{left:358px;top:1487px;width:254px;height:287px;background:linear-gradient(160deg,#9aa0a8,#c9a185 50%,#5d7f9c)}
.photo-cafe{left:612px;top:1487px;width:508px;height:575px;background:linear-gradient(110deg,#d9d4ca 0%,#c6b9a6 40%,#7b6350 70%,#3c3530 100%)}
.tile-about{left:79px;top:1774px;width:279px;height:288px}
.tile-about h4{position:absolute;left:50px;top:90px;font-weight:400;font-size:21px;line-height:24px}
.tile-about p{position:absolute;left:49px;top:150px;width:210px;font-size:15px;line-height:19px;color:var(--grey)}
.tile-about a{position:absolute;left:50px;top:209px;font-size:13px;font-weight:600;color:var(--pink);letter-spacing:.5px}
.tile-pink{left:358px;top:1774px;width:254px;height:288px;background:var(--pink);color:var(--white)}
.tile-pink h4{position:absolute;left:45px;top:89px;font-weight:400;font-size:20px;line-height:24px}
.tile-pink .phone{position:absolute;left:48px;top:141px;font-size:22px}
.tile-pink a{position:absolute;left:50px;top:193px;font-size:13px;font-weight:600;border-bottom:2px solid var(--white);padding:0 2px 3px;letter-spacing:.5px}
.tile-cafe{left:613px;top:1776px;width:311px;height:286px;background:rgba(255,255,255,.93);border:2px solid var(--ink)}
.tile-cafe h4{position:absolute;left:37px;top:97px;font-weight:400;font-size:21px}
.tile-cafe p{position:absolute;left:37px;top:136px;width:260px;font-size:14px;line-height:22px;color:#444}
.tile-cafe a{position:absolute;left:38px;top:194px;font-size:13px;font-weight:600;border-bottom:2px solid var(--ink);padding-bottom:3px;letter-spacing:.5px}

/* footer */
.footer{left:0;top:2227px;width:1200px;height:552px;background:var(--blue);color:var(--white)}
.footer .brand{left:472px;top:62px}
.footer .brand-dot{border-color:var(--white)}
.badge{top:163px;height:61px;background:var(--white)}
.badge.dark{background:#1d3e8f}
.footer .rule{left:79px;top:282px;width:1041px;height:1px;background:rgba(255,255,255,.7)}
.footer h5{position:absolute;left:0;right:0;top:315px;text-align:center;font-weight:400;font-size:24px}
.footer .intro{position:absolute;left:0;right:0;top:362px;text-align:center;font-size:16px;line-height:20px}
.subscribe{left:381px;top:422px;width:466px;height:45px;border:2px solid var(--white);display:flex}
.subscribe .field{flex:1;font-size:14px;font-weight:500;padding:12px 13px}
.subscribe .go{width:162px;background:var(--pink);font-size:16px;font-weight:500;text-align:center;padding-top:10px}

.legal{left:106px;top:2810px;font-size:14px;line-height:20px;color:var(--grey)}
.social{top:2815px;width:40px;height:40px;border-radius:3px}
.bottom-rule{left:0;top:2889px;width:1200px;height:1px;background:#e3e3e3}
.copyright{left:0;width:1200px;top:2928px;text-align:center;font-size:13px;color:#444}
</style>
</head>
<body>

<header>
  <div class="abs contact"><b>Contact us :</b> 03 9000 4172<br><b>Email id:</b> admin@tarvolnh.org.au</div>
  <div class="abs brand"><span class="brand-dot"></span><span class="brand-name">Tarvol Neighbourhood Learning Centre</span></div>
  <div class="abs search"><span>Search here</span>
    <svg width="14" height="14" viewBox="0 0 14 14"><circle cx="6" cy="6" r="4.5" fill="none" stroke="#222" stroke-width="1.6"/><line x1="9.3" y1="9.3" x2="13" y2="13" stroke="#222" stroke-width="1.6"/></svg>
  </div>
  <nav class="abs nav">
    <a class="active">Home</a><a>Courses</a><a>Social Enterprise</a><a>Community Programs</a><a>Tarvol Cares</a><a>Venue Hire</a><a>Sidechair Café</a>
  </nav>
</header>

<section class="hero">
  <div class="abs donate">
    <h2>Support us<br>with a donation</h2>
    <p>Your donation will be directed towards&nbsp; the program of your choosing. All donations tax deductible</p>
    <a class="link">Donate Now <svg class="arrow" width="30" height="10" viewBox="0 0 30 10"><path d="M0 5H28M23 1L28 5L23 9" fill="none" stroke="#333" stroke-width="1.5"/></svg></a>
  </div>
  <div class="abs hero-photo" role="img" aria-label="Two smiling schoolgirls at a classroom desk"></div>
  <svg class="abs hero-nav" width="60" height="30" viewBox="0 0 60 30"><path d="M14 2L4 15L14 28M46 2L56 15L46 28" fill="none" stroke="#fff" stroke-width="2.5"/></svg>
  <div class="abs hero-card">
    <h3>Learning<br>makes us smile</h3>
    <p>Our accredited Childcare and Kinder allows your child to grown in a fun learning environment, while you attend courses or</p>
    <a class="btn-pink"><svg width="30" height="20" viewBox="0 0 30 20"><path d="M15 4C11 1 6 1 2 2V18C6 17 11 17 15 19C19 17 24 17 28 18V2C24 1 19 1 15 4ZM15 4V19" fill="none" stroke="#fff" stroke-width="1.6"/></svg>Start learning now</a>
  </div>
</section>

<section class="courses">
  <h2 class="abs section-title">Courses we offer</h2>
  <a class="abs btn-outline">Enroll Now <svg class="arrow" width="30" height="10" viewBox="0 0 30 10"><path d="M0 5H28M23 1L28 5L23 9" fill="none" stroke="#ec1e79" stroke-width="1.5"/></svg></a>
  <div class="abs pager" style="left:1004px"><svg width="22" height="10" viewBox="0 0 22 10"><path d="M22 5H2M7 1L2 5L7 9" fill="none" stroke="#222" stroke-width="1.5"/></svg></div>
  <div class="abs pager" style="left:1051px"><svg width="22" height="10" viewBox="0 0 22 10"><path d="M0 5H20M15 1L20 5L15 9" fill="none" stroke="#222" stroke-width="1.5"/></svg></div>

  <article class="abs course" style="left:106px;width:215px"><div class="thumb" role="img" aria-label="Children at computers in a coding club" style="background:linear-gradient(135deg,#cfd6d8,#8a9aa2 50%,#5a6b77)"></div><span>Kids coding club</span></article>
  <article class="abs course" style="left:344px;width:233px"><div class="thumb" role="img" aria-label="Hands typing on a keyboard" style="background:linear-gradient(135deg,#a16b45,#5b3b28 50%,#2b2420)"></div><span>Digital Literacy for EAL</span></article>
  <article class="abs course" style="left:599px;width:234px"><div class="thumb" role="img" aria-label="Older learners in a computer room" style="background:linear-gradient(135deg,#6f7b86,#bfc4c8 50%,#8c8f94)"></div><span>IT for Beginners</span></article>
  <article class="abs course" style="left:856px;width:234px"><div class="thumb" role="img" aria-label="Person seated in a yoga pose" style="background:linear-gradient(135deg,#3f3a47,#857b82 50%,#b9aab0)"></div><span>Evening Yoga Class</span></article>
</section>

<section>
  <p class="abs video">Check out our new Vidmo and Tubely channels!<br>Now you can view all the amazing work that goes on at TNLC</p>
  <a class="abs video-link">TNLC Short films</a>
</section>

<section class="grid">
  <div class="abs tile-blue"><h4>Community<br>programs</h4><a>View Details <svg class="arrow" width="26" height="10" viewBox="0 0 26 10"><path d="M0 5H24M19 1L24 5L19 9" fill="none" stroke="#fff" stroke-width="1.5"/></svg></a></div>
  <div class="abs photo-hands" role="img" aria-label="Group of people joining hands in a circle"></div>
  <div class="abs photo-cafe" role="img" aria-label="Young man preparing food in a cafe kitchen"></div>
  <div class="abs tile-about"><h4>Tarvol Neighbourhood<br>Learning Center</h4><p>We provide courses for everyone in the community</p><a>Enroll Now</a></div>
  <div class="abs tile-pink"><h4>For any query<br>Call us on</h4><div class="phone">03 9000 4172</div><a>View Course Brochure</a></div>
  <div class="abs tile-cafe"><h4>Chairing is Caring</h4><p>Just a small cafe with a big heart, soul and always a sidechair!</p><a>Sidechair Cafe <svg class="arrow" width="26" height="10" viewBox="0 0 26 10"><path d="M0 5H24M19 1L24 5L19 9" fill="none" stroke="#222" stroke-width="1.5"/></svg></a></div>
</section>

<footer class="abs footer">
  <div class="abs brand"><span class="brand-dot"></span><span class="brand-name">Tarvol Neighbourhood Learning Centre</span></div>
  <div class="abs badge dark" style="left:434px;width:107px"></div>
  <div class="abs badge" style="left:555px;width:113px"></div>
  <div class="abs badge" style="left:683px;width:80px"></div>
  <div class="abs rule"></div>
  <h5>Sign up to our Newsletter</h5>
  <p class="intro">We send news about our courses, community programs, child care, cafe &amp; special<br>events approximately 10 times a year.</p>
  <div class="abs subscribe"><div class="field">Email Id:</div><div class="go">Subscribe</div></div>
</footer>

<p class="abs legal">Tarvol Neighbourhood Learning Centre Inc is registered as a charity<br>with the National Register of Charities and Not-for-profits<br>ABN 12 345 678 901.</p>
<div class="abs social" style="left:892px;background:#3b5998"></div>
<div class="abs social" style="left:945px;background:#3f729b"></div>
<div class="abs social" style="left:998px;background:#35465c"></div>
<div class="abs social" style="left:1052px;background:#1ab7ea"></div>
<div class="abs bottom-rule"></div>
<p class="abs copyright">© 2019 Tarvol Neighbourhood Learning Centre. All Rights Reserved. Policies &amp; Procedures.</p>

</body>
</html>
```